Young Accounting firm needing a captivating business card

We need a business card design that forces the person to look at the card because its either gold foil, plastic, or lettering pop up etc. We already have a logo with a specific gold color and we need to make it pop. We are an accounting firm. I need the words" accounting, payroll, licenses, audits, taxes" somewhere on the business card so as to describe what we do- preferably on the side where the logo is at.

Industry/Entity Type

Accounting

Contact Information for Business Card

Address 48276 9th Ave S Ste 305, Federal Way, WA 98117
Business Phone (360)418-2096
Fax (360)418-2157
Office Cell Phone (360)586-7319

Font styles to use
Serif

Colors
85abd2

Requirements
Must have
• It should state
• "Accounting" "Taxes" "Audits" "Licenses" "Payroll"
Nice to have
• Matte with gold foil, different textures, With Either a textured ivory background or gray blue slate background
Should not have
• colorful colors

```html
<!DOCTYPE html>
<html lang="en">
<head>
<meta charset="utf-8">
<title>Ledgerline Business Card</title>
<link href="https://fonts.googleapis.com/css2?family=Lexend:wght@500;600&family=Arimo:wght@400&display=swap" rel="stylesheet">
<style>
  :root {
    --navy: #0e3b60;
    --gold: #b99a2e;
    --icon-blue: #2aa3df;
    --white: #ffffff;
    --page: #ffffff;
  }
  * { margin: 0; padding: 0; box-sizing: border-box; }
  html, body { width: 848px; height: 1200px; overflow: hidden; background: var(--page); }
  .canvas { position: relative; width: 848px; height: 1200px; }

  .card {
    position: absolute;
    left: 127px;
    width: 588px;
    height: 336px;
    background: var(--navy);
    border-radius: 26px;
    overflow: hidden;
    box-shadow: 6px 6px 8px rgba(0,0,0,0.35);
  }
  .card--front { top: 233px; }
  .card--back { top: 623px; }

  .brand-name {
    position: absolute;
    font-family: "Lexend", sans-serif;
    font-weight: 500;
    color: var(--gold);
    letter-spacing: -1px;
    line-height: 1;
  }
  .card--front .brand-name {
    left: 0; right: 0; top: 166px;
    text-align: center;
    font-size: 31px;
  }
  .brand-rule {
    position: absolute;
    left: 130px; top: 207px;
    width: 334px; height: 1.5px;
    background: var(--gold);
  }
  .services {
    position: absolute;
    left: 0; right: 0; top: 214px;
    text-align: center;
    font-family: "Lexend", sans-serif;
    font-weight: 500;
    font-size: 16px;
    color: var(--gold);
    word-spacing: 3px;
  }

  .card--back .brand-name { left: 39px; top: 102px; font-size: 31px; }

  .person { position: absolute; right: 80px; top: 131px; text-align: right; }
  .person-name {
    font-family: "Lexend", sans-serif;
    font-weight: 600;
    font-size: 26px;
    color: var(--gold);
    line-height: 1;
  }
  .person-title {
    font-family: "Arimo", sans-serif;
    font-size: 11.5px;
    color: var(--white);
    margin-top: 3px;
  }

  .contact {
    position: absolute;
    font-family: "Arimo", sans-serif;
    font-size: 15px;
    line-height: 19px;
    color: var(--white);
    display: flex;
    align-items: flex-start;
  }
  .contact svg { position: absolute; left: -26px; top: 1px; }
  .contact--address { left: 166px; top: 206px; }
  .contact--phone { left: 166px; top: 254px; }
  .contact--fax { left: 166px; top: 285px; }
  .contact--cell { left: 384px; top: 208px; }
  .contact--email { left: 384px; top: 241px; }

  .web-band { position: absolute; left: 0; top: 0; }
  .web-address {
    position: absolute;
    left: 295px; right: 0; top: 312px;
    text-align: center;
    font-family: "Arimo", sans-serif;
    font-size: 20px;
    color: var(--white);
    line-height: 1;
  }
</style>
</head>
<body>
<main class="canvas">

  <section class="card card--front">
    <div class="brand-name">Ledgerline</div>
    <div class="brand-rule"></div>
    <p class="services">Accounting Taxes Audits Licenses Payroll</p>
  </section>

  <section class="card card--back">
    <div class="brand-name">Ledgerline</div>

    <div class="person">
      <div class="person-name">Name Here</div>
      <div class="person-title">Director</div>
    </div>

    <p class="contact contact--address">
      <svg width="14" height="18" viewBox="0 0 14 18" aria-hidden="true"><path d="M7 0C3.1 0 0 3 0 6.8 0 11.5 7 18 7 18s7-6.5 7-11.2C14 3 10.9 0 7 0z" fill="var(--icon-blue)"/><circle cx="7" cy="6.7" r="2.6" fill="var(--navy)"/></svg>
      <span>48276 9th Ave S Ste 305,<br>Federal Way, WA 98117.</span>
    </p>
    <p class="contact contact--phone">
      <svg width="16" height="16" viewBox="0 0 16 16" aria-hidden="true"><path d="M3.2 0.5l2.4 3.1c.4.5.3 1.1-.1 1.5L4.3 6.2c.9 2.2 3.2 4.6 5.5 5.5l1.1-1.2c.4-.4 1-.5 1.5-.1l3.1 2.4c.5.4.5 1 .1 1.5l-1.3 1.3C12 17 .6 6.1 1.9 1.7L3.2.5z" fill="var(--icon-blue)"/></svg>
      <span>(360)418-2096</span>
    </p>
    <p class="contact contact--fax">
      <svg width="18" height="17" viewBox="0 0 18 17" aria-hidden="true"><rect x="4" y="0" width="10" height="4" fill="var(--icon-blue)"/><rect x="0" y="5" width="18" height="8" rx="2" fill="var(--icon-blue)"/><rect x="4" y="9" width="10" height="8" fill="var(--icon-blue)" stroke="var(--navy)" stroke-width="1.2"/><line x1="6" y1="12" x2="12" y2="12" stroke="var(--navy)"/><line x1="6" y1="14.5" x2="12" y2="14.5" stroke="var(--navy)"/></svg>
      <span>(360)418-2157</span>
    </p>
    <p class="contact contact--cell">
      <svg width="12" height="18" viewBox="0 0 12 18" aria-hidden="true"><rect x="1" y="1" width="10" height="16" rx="1.5" fill="none" stroke="var(--icon-blue)" stroke-width="1.6"/><circle cx="6" cy="14.3" r="0.9" fill="var(--icon-blue)"/></svg>
      <span>(360)586-7319</span>
    </p>
    <p class="contact contact--email">
      <svg width="18" height="13" viewBox="0 0 18 13" aria-hidden="true" style="top:4px"><rect x="0" y="0" width="18" height="13" fill="var(--icon-blue)"/><path d="M0 0l9 7 9-7M0 13l6.5-6M18 13l-6.5-6" fill="none" stroke="var(--navy)" stroke-width="1"/></svg>
      <span>info@ledgerlinetax.com</span>
    </p>

    <svg class="web-band" width="588" height="336" viewBox="0 0 588 336" aria-hidden="true">
      <path d="M308 336 L318 318 Q323 311 333 311 L588 311 L588 336 Z" fill="var(--gold)"/>
    </svg>
    <div class="web-address">www.ledgerlinetax.com</div>
  </section>

</main>
</body>
</html>
```